Security and Staff Identity Business Products Brochure is required.

Looking for a brochure that introduces the business, and the general products and categories we sell.

The flyer will be 2 sided A3 in size, which will be folded in half once printed to effectively be 4 printed sides. 420 x 297mm

I have a lumen-crate account - if there is images you would like to use and i like the design i can purchase them.

As the finalised contact details have not yet available, please ensure that the final contact design can be edited for contact details - Phone, address, email etc.

Content is in the attached files. Ideally the front page will have logo, image/s, and our 3x Value pillars "Global Brands", "Local Supply", "Expert Advice".
Inside will have the 4 product lines w/ content and relevant images.

I have attached an similar brochure for the idea - Titles Tavorn Brochure. PLEASE Note i am after a far more sophisticated and professional looking brochure than this.

Target Market(s)

Potential new customers who need to be introduced to who we are and what range of products we supply

Industry/Entity Type

Security

Other font styles liked:
• Calibri

Colors
abd037
ffffff
919191
1b1b1b
474747
9bcb3c

Requirements
Must have
• Must have 4 categories shown on the inside page/s. Printers, Printer Ribbons, Cards & Access, and Accessories.
• Show the supplier logo's we supply.
• Some not necessarily all corresponding images to those categories.
• Text content in the IDbrochure.docx attachment.
• Must be: 2 sided A3 in size, which will be folded in half once printed to effectively be 4 printed sides. 420 x 297mm
• x Value pillars "Global Brands", "Local Supply", "Expert Advice"
• Colours as per business card and logo design attached.
Nice to have
• Nice to have some background images from Lumen Crate or similar. Business people walking through a business environment.
Should not have
• No cartoons

```html
<!DOCTYPE html>
<html lang="en">
<head>
<meta charset="utf-8">
<title>Cardwell Group Brochure</title>
<link rel="stylesheet" href="https://fonts.googleapis.com/css2?family=Russo+One&family=Montserrat:wght@400;500;600&family=Oswald:wght@600&display=swap">
<style>
:root{
  --green:#abd037;
  --green-2:#9bcb3c;
  --white:#ffffff;
  --grey:#919191;
  --ink:#1b1b1b;
  --slate:#474747;
  --panel:#2b2b2d;
  --bg:#e9e9e9;
}
*{box-sizing:border-box;margin:0;padding:0}
html,body{width:1200px;height:1200px;overflow:hidden;background:var(--bg);font-family:"Montserrat",sans-serif}
.spread{position:absolute;left:200px;width:800px;height:566px;overflow:hidden;box-shadow:0 4px 14px rgba(0,0,0,.25)}
.spread--outer{top:24px}
.spread--inner{top:610px;background:var(--panel)}
.page{position:absolute;top:0;width:400px;height:566px;overflow:hidden}
.page--back{left:0;background:var(--panel)}
.page--front{left:400px;background:var(--panel)}
.photo{position:absolute;border-radius:50%;overflow:hidden}
.deco{position:absolute;inset:0}
.web-tab{position:absolute;font-size:9px;color:var(--ink);font-weight:600;white-space:nowrap}
.wordmark{position:absolute;font-family:"Montserrat",sans-serif;font-weight:500;color:var(--green);font-size:22px;letter-spacing:-.5px;line-height:1;white-space:nowrap}
.contact{position:absolute;left:120px;top:470px;font-size:9px;line-height:1.5;color:var(--green)}
.pillars{position:absolute;left:8px;top:16px;display:flex;flex-direction:column;gap:8px;align-items:flex-start}
.pillar{background:var(--green);color:var(--ink);font-family:"Russo One",sans-serif;font-size:17px;padding:6px 7px;line-height:1}
.front__title{position:absolute;top:406px;width:100%;text-align:center;color:var(--white);font-family:"Montserrat",sans-serif;font-weight:600;font-size:17px;letter-spacing:.6px}
.front__rule{position:absolute;top:434px;left:180px;width:40px;height:2px;background:var(--green)}
.front__text{position:absolute;top:446px;left:30px;width:340px;text-align:center;font-size:6px;line-height:1.6;color:var(--grey)}
.suppliers__title{position:absolute;top:12px;width:100%;text-align:center;font-family:"Russo One",sans-serif;font-size:12px;color:var(--ink)}
.supplier{position:absolute;font-family:"Montserrat",sans-serif;font-weight:600;font-size:14px;color:var(--slate)}
.section{position:absolute;width:230px}
.section__title{font-family:"Russo One",sans-serif;color:var(--green);font-size:11px;line-height:1.15;margin-bottom:8px}
.section__text{font-size:6.2px;line-height:1.65;color:#cfcfcf;margin-bottom:6px}
.divider{position:absolute;height:1px;background:var(--green);width:140px}
.phone{position:absolute;top:522px;width:100%;text-align:center;font-family:"Oswald",sans-serif;font-size:22px;color:var(--green)}
</style>
</head>
<body>

<section class="spread spread--outer" aria-label="Brochure outer spread">

  <div class="page page--back">
    <svg class="deco" viewBox="0 0 400 566" aria-hidden="true">
      <polygon points="0,0 400,0 400,140 0,0" fill="#f2f2f2"/>
      <polygon points="0,-2 400,138 400,146 0,6" fill="#ffffff"/>
      <path d="M0,420 C120,380 260,470 400,440 L400,566 L0,566 Z" fill="#333335"/>
      <path d="M0,440 C140,400 260,490 400,460" fill="none" stroke="#3c3c3e" stroke-width="1"/>
    </svg>
    <div class="web-tab" style="left:120px;top:30px;transform:rotate(19deg);background:#fff;padding:3px 16px">www.cardwellgroup.com</div>
    <div class="photo" style="left:-110px;top:70px;width:330px;height:330px;border:9px solid var(--green);box-shadow:0 0 0 4px #fff inset">
      <div role="img" aria-label="Photograph of a hand moving a black chess piece" style="width:100%;height:100%;background:radial-gradient(circle at 55% 45%,#f4f4f4 0%,#cfcfcf 55%,#2e3440 100%)"></div>
    </div>
    <div class="wordmark" style="left:18px;top:412px">Cardwell Group</div>
    <div class="contact">
      214 Harbor Lane, Westfield, CA 90210 United States<br>
      + 1800 555 014<br>
      info@cardwellgroup.com
    </div>
  </div>

  <div class="page page--front">
    <svg class="deco" viewBox="0 0 400 566" aria-hidden="true">
      <defs>
        <linearGradient id="frontTop" x1="0" y1="0" x2="1" y2="0">
          <stop offset="0" stop-color="#ffffff"/>
          <stop offset="1" stop-color="#dcdcdc"/>
        </linearGradient>
      </defs>
      <path d="M0,0 L400,0 L400,345 C300,380 120,385 0,335 Z" fill="#8a8a8a"/>
      <path d="M0,0 L400,0 L400,332 C300,368 120,372 0,322 Z" fill="url(#frontTop)"/>
    </svg>
    <div class="pillars">
      <span class="pillar">Global Brands</span>
      <span class="pillar">Local Supply</span>
      <span class="pillar">Expert Advice</span>
    </div>
    <div class="photo" style="left:190px;top:30px;width:230px;height:230px;border:7px solid #7a7a7a">
      <div role="img" aria-label="Photograph of business people reviewing a tablet together" style="width:100%;height:100%;background:linear-gradient(160deg,#b9c6cf 0%,#5d6670 50%,#1f2328 100%)"></div>
    </div>
    <div class="photo" style="left:88px;top:200px;width:200px;height:200px;border:7px solid #7a7a7a">
      <div role="img" aria-label="Photograph of smiling colleagues applauding in a meeting" style="width:100%;height:100%;background:linear-gradient(140deg,#e8e6e2 0%,#a9a39a 50%,#3a3a3c 100%)"></div>
    </div>
    <h1 class="front__title">Dedicated Virtual Assistants</h1>
    <div class="front__rule"></div>
    <p class="front__text">We pair every client with a dedicated assistant who handles quotes, orders and follow-up so your ID program keeps running without delay.</p>
    <div class="wordmark" style="right:20px;top:512px">Cardwell Group</div>
  </div>
</section>

<section class="spread spread--inner" aria-label="Brochure inner spread">
  <svg class="deco" viewBox="0 0 800 566" aria-hidden="true">
    <defs>
      <linearGradient id="innerTop" x1="0" y1="0" x2="1" y2="0">
        <stop offset="0" stop-color="#ffffff"/>
        <stop offset="0.5" stop-color="#e6e7ea"/>
        <stop offset="1" stop-color="#f4f4f4"/>
      </linearGradient>
    </defs>
    <path d="M0,0 L800,0 L800,70 C650,180 150,180 0,70 Z" fill="var(--green)"/>
    <path d="M0,0 L800,0 L800,62 C650,170 150,170 0,62 Z" fill="url(#innerTop)"/>
    <path d="M0,500 C200,470 500,480 800,530 L800,566 L0,566 Z" fill="#343436"/>
    <line x1="400" y1="145" x2="400" y2="566" stroke="#3a3a3c" stroke-width="1"/>
  </svg>
  <div class="web-tab" style="left:90px;top:2px;background:var(--green);padding:2px 16px;font-size:8px">www.cardwellgroup.com</div>
  <div class="web-tab" style="left:500px;top:2px;background:var(--green);padding:2px 16px;font-size:8px">www.cardwellgroup.com</div>
  <h2 class="suppliers__title">Our Suppliers</h2>
  <span class="supplier" style="left:248px;top:36px">Veral</span>
  <span class="supplier" style="left:338px;top:36px">Torvix</span>
  <span class="supplier" style="left:434px;top:36px">Quillon</span>
  <span class="supplier" style="left:300px;top:60px">Brenmark</span>
  <span class="supplier" style="left:405px;top:60px">Ostrana</span>

  <div class="photo" style="left:100px;top:60px;width:130px;height:130px;border:5px solid var(--green);background:#fff">
    <div role="img" aria-label="Product photo of a red lanyard" style="width:100%;height:100%;background:radial-gradient(circle,#e35a5a 0%,#f3d5d5 45%,#ffffff 70%)"></div>
  </div>
  <div class="photo" style="left:308px;top:150px;width:184px;height:184px;border:6px solid var(--green);background:#fff">
    <div role="img" aria-label="Product photo of an ID card printer" style="width:100%;height:100%;background:radial-gradient(circle,#5a5d62 0%,#9a9da2 40%,#ffffff 68%)"></div>
  </div>
  <div class="photo" style="left:535px;top:60px;width:130px;height:130px;border:5px solid var(--green);background:#fff">
    <div role="img" aria-label="Product photo of a colour printer ribbon cartridge" style="width:100%;height:100%;background:radial-gradient(circle,#2a2a2a 0%,#7a6fb0 35%,#ffffff 68%)"></div>
  </div>
  <div class="photo" style="left:325px;top:350px;width:150px;height:150px;border:5px solid #fff;background:#fff">
    <div role="img" aria-label="Product photo of RFID wristbands in green, red and blue" style="width:100%;height:100%;background:radial-gradient(circle,#d94040 0%,#3b9a4a 35%,#2d4aa0 55%,#ffffff 72%)"></div>
  </div>

  <div class="section" style="left:48px;top:210px">
    <h3 class="section__title">ID Card Printers</h3>
    <p class="section__text">Whether you need a plastic card printer for staff ID, membership cards or secure access cards, we supply trusted models from the world's leading makers so you get reliable hardware.</p>
    <p class="section__text">With ID card systems from us you take a critical step toward a more secure workplace, with options for every application and budget.</p>
  </div>
  <div class="divider" style="left:100px;top:330px"></div>
  <div class="section" style="left:40px;top:348px">
    <h3 class="section__title">Printer Ribbons and<br>Maintenance</h3>
    <p class="section__text">We supply printer ribbons for many models, whether you print single sided, double sided, colour or monochrome. Talk to us today and let us help you pick the right ribbons.</p>
    <p class="section__text">Card printers need care and regular maintenance to run at peak performance. Our cleaning kits make upkeep easy.</p>
  </div>

  <div class="section" style="left:520px;top:210px">
    <h3 class="section__title">Cards<br>and Access Control</h3>
    <p class="section__text">We supply genuine access control cards. If you run an existing proximity or smart card system, ask us for a quote. Looking for key fobs or wristbands? We bring the same level of advice and service.</p>
  </div>
  <div class="divider" style="left:570px;top:330px"></div>
  <div class="section" style="left:520px;top:348px">
    <h3 class="section__title">ID Accessories</h3>
    <p class="section__text">We offer a wide range of card holders, lanyards, retractable reels, clips and badges made from quality materials. We can also customise accessories with your corporate logo and branding.</p>
  </div>

  <div class="wordmark" style="left:40px;top:526px">Cardwell Group</div>
  <div class="phone">+ 1800 555 014</div>
  <div class="wordmark" style="right:40px;top:526px">Cardwell Group</div>
</section>

</body>
</html>
```